Business Card Design Project

Business card design based on the existing logo.
Updates

Target Market(s)

Small to medium business owners and CIO's looking for professional IT services.

Industry/Entity Type

Business

Font styles to use
Serif
Sans Serif

Requirements
Must have
• Logo, company name, company details

Text to appear on the business card
Name / Title:
Tom Whitlock
CEO

Address:
Veltra Limited
Level 1, 482 Korau Rd
P O Box 362
Ohakune 5918

Other details:
tom@veltra.co
Ph: 0800 519 306
Mob: +64 21 948 213
www.veltra.co

Nice to have
• I would look at both single and double sided options. My initial thought is double sided with just the logo with the grey framing for the front and the name and details on the back. But I'm open to other design options.

```html
<!DOCTYPE html>
<html lang="en">
<head>
<meta charset="utf-8">
<title>Tenvaro Business Card</title>
<link rel="stylesheet" href="https://fonts.googleapis.com/css2?family=Jost:wght@400;500;600&display=swap">
<style>
  :root {
    --backdrop: #2b2b2d;
    --card-blue: #1f6e8e;
    --card-blue-deep: #185a76;
    --card-white: #ffffff;
    --card-white-shade: #eeeeee;
    --ink-teal: #1d5f7d;
    --ink-grey: #4a4a4a;
    --rule-grey: #9a9a9a;
    --on-blue: #ffffff;
  }
  * { margin: 0; padding: 0; box-sizing: border-box; }
  html, body {
    width: 1200px; height: 900px; overflow: hidden;
    background: var(--backdrop);
    font-family: "Jost", sans-serif;
  }
  .stage {
    width: 1200px; height: 900px;
    display: flex; flex-direction: column; align-items: center; justify-content: center;
    gap: 44px;
  }
  .card {
    width: 640px; height: 366px;
    position: relative;
    box-shadow: 0 12px 30px rgba(0,0,0,0.45);
  }
  .card--front {
    background: linear-gradient(135deg, var(--card-blue) 0%, var(--card-blue-deep) 100%);
    color: var(--on-blue);
  }
  .front-brand {
    position: absolute; right: 48px; bottom: 56px; text-align: left;
  }
  .front-brand__name {
    font-size: 54px; font-weight: 500; line-height: 1; letter-spacing: 0.5px;
  }
  .front-brand__url {
    margin-top: 10px; font-size: 17px; font-weight: 500; letter-spacing: 1px;
  }
  .card--back {
    background: linear-gradient(180deg, var(--card-white) 40%, var(--card-white-shade) 100%);
    color: var(--ink-grey);
  }
  .back-brand {
    position: absolute; top: 42px; left: 0; right: 0;
    display: flex; justify-content: center; align-items: center; gap: 12px;
  }
  .back-brand__mark {
    width: 18px; height: 18px; border-radius: 50%; background: var(--ink-teal);
  }
  .back-brand__name {
    font-size: 42px; font-weight: 500; color: var(--ink-teal); line-height: 1;
  }
  .person {
    position: absolute; left: 150px; top: 162px;
  }
  .person__name {
    font-size: 23px; font-weight: 600; color: var(--ink-teal); letter-spacing: 0.5px;
  }
  .person__title {
    font-size: 20px; font-weight: 400; color: var(--ink-grey); line-height: 1.1;
  }
  .divider {
    position: absolute; left: 392px; top: 128px; width: 1px; height: 178px;
    background: var(--rule-grey);
  }
  .details {
    position: absolute; left: 418px; top: 130px;
    font-size: 17px; line-height: 1.3; color: var(--ink-grey);
  }
  .details address { font-style: normal; }
  .detail-row { display: flex; gap: 14px; align-items: flex-start; }
  .detail-row + .detail-row { margin-top: 14px; }
  .detail-icons { display: flex; flex-direction: column; gap: 5px; padding-top: 4px; }
  .icon { width: 16px; height: 17px; fill: var(--ink-teal); display: block; }
</style>
</head>
<body>
<main class="stage">
  <section class="card card--front" aria-label="Card front">
    <div class="front-brand">
      <div class="front-brand__name">Tenvaro</div>
      <div class="front-brand__url">www.veltra.co</div>
    </div>
  </section>

  <section class="card card--back" aria-label="Card back">
    <div class="back-brand">
      <span class="back-brand__mark"></span>
      <span class="back-brand__name">Tenvaro</span>
    </div>

    <div class="person">
      <div class="person__name">TOM WHITLOCK</div>
      <div class="person__title">CEO</div>
    </div>

    <div class="divider"></div>

    <div class="details">
      <div class="detail-row">
        <div class="detail-icons">
          <svg class="icon" viewBox="0 0 16 17" aria-hidden="true"><path d="M8 0a6 6 0 0 0-6 6c0 4.5 6 11 6 11s6-6.5 6-11a6 6 0 0 0-6-6zm0 8.5A2.5 2.5 0 1 1 8 3.5a2.5 2.5 0 0 1 0 5z"/></svg>
        </div>
        <address>
          Veltra Limited<br>
          Level 1, 482 Korau Rd<br>
          P O Box 362<br>
          Ohakune 5918
        </address>
      </div>
      <div class="detail-row">
        <div class="detail-icons">
          <svg class="icon" viewBox="0 0 16 17" aria-hidden="true"><path d="M0 4h16v10H0zM1.5 5.5v.3L8 10l6.5-4.2v-.3z"/></svg>
          <svg class="icon" viewBox="0 0 16 17" aria-hidden="true"><path d="M1 6c0-2 3-3 7-3s7 1 7 3v1.5h-3.5V6h-7v1.5H1zM3 8.5h10l1 7H2zM8 10a2 2 0 1 0 0 4 2 2 0 0 0 0-4z"/></svg>
          <svg class="icon" viewBox="0 0 16 17" aria-hidden="true"><path d="M4 0h8a1 1 0 0 1 1 1v15a1 1 0 0 1-1 1H4a1 1 0 0 1-1-1V1a1 1 0 0 1 1-1zm1 2v5h6V2zm0 7v1.5h1.5V9zm2.3 0v1.5h1.5V9zm2.2 0v1.5H11V9zM5 11.5V13h1.5v-1.5zm2.3 0V13h1.5v-1.5zm2.2 0V13H11v-1.5z"/></svg>
        </div>
        <div>
          tom@veltra.co<br>
          0800 519 306<br>
          +64 21 948 213
        </div>
      </div>
    </div>
  </section>
</main>
</body>
</html>
```